brisk-vale.com Real Estate, Investment, Financial corporate

Real Estate, Investment, Financial corporate looking site. Show present a professional firm, with an elegant display. Please see the attached file which includes the logo, palette and fonts.
Updates

We just starting the brief today. ( logo was delayed)

Target Market(s)

Investors, Corporate , B2b

Industry/Entity Type

real-estate investments

Number of Pages Required

3 page

Requirements
Must have
• Dazzling Homepage
Nice to have
• paralex

```html
<!DOCTYPE html>
<html lang="en">
<head>
<meta charset="utf-8">
<title>Brisk Vale — Property Investment Company</title>
<link href="https://fonts.googleapis.com/css2?family=Libre+Baskerville&family=Lato:wght@400;700&display=swap" rel="stylesheet">
<style>
:root{
  --dark:#262626;
  --dark-2:#2e2e2e;
  --peach:#f2c994;
  --peach-2:#e6bf8c;
  --gold:#e7b67a;
  --ink:#1f1f1f;
  --muted:#555;
  --white:#ffffff;
  --serif:"Libre Baskerville", Georgia, serif;
  --sans:"Lato", Arial, sans-serif;
}
*{box-sizing:border-box;margin:0;padding:0}
html,body{width:1200px;height:5352px;overflow:hidden}
body{position:relative;background:var(--dark);font-family:var(--sans);color:var(--white)}
.abs{position:absolute}
.serif{font-family:var(--serif)}
.btn{position:absolute;display:flex;align-items:center;justify-content:space-between;border-radius:30px;padding:0 6px 0 26px;font-size:15px;white-space:nowrap}
.btn .dot{width:30px;height:30px;border-radius:50%;display:flex;align-items:center;justify-content:center}
.btn-peach{background:var(--peach);color:var(--ink)}
.btn-peach .dot{background:var(--ink)}
.btn-dark{background:var(--dark);color:var(--white)}
.btn-dark .dot{background:var(--white)}

/* header */
.site-header{left:0;top:0;width:1200px;height:152px;background:var(--dark)}
.brand{position:absolute;display:flex;flex-direction:column;align-items:center;font-family:var(--serif);color:var(--gold);white-space:nowrap}
.brand-square{width:40px;height:40px;border:3px solid var(--gold);margin-bottom:8px}
.brand-name{font-size:30px}
.nav a{position:absolute;top:68px;font-size:15px;color:var(--white);text-decoration:none}
.nav a.active{color:var(--gold);border-bottom:2px solid var(--gold);padding-bottom:8px}

/* hero */
.hero{left:0;top:152px;width:1200px;height:800px;overflow:hidden}
.hero-photo{position:absolute;inset:0;background:linear-gradient(160deg,#8ea2b6 0%,#3f4f62 35%,#1f2a36 65%,#6b4a2a 100%)}
.hero-title{position:absolute;left:98px;top:308px;font-family:var(--serif);font-size:34px;line-height:58px;color:var(--peach);letter-spacing:1px;font-weight:400}
.search-panel{position:absolute;left:720px;top:147px;width:380px;height:465px;background:linear-gradient(135deg,rgba(120,130,140,.75),rgba(40,44,50,.85))}
.search-head{height:77px;background:var(--peach);color:var(--ink);text-align:center;font-family:var(--serif);font-size:22px;padding-top:20px;letter-spacing:1px}
.search-head small{display:block;font-size:9px;letter-spacing:1px;margin-top:4px;color:#5a4a38}
.field-label{position:absolute;left:52px;font-size:15px}
.select{position:absolute;left:52px;width:278px;height:50px;background:#1a1a1a;border:1px solid #555;font-size:15px;padding:15px 14px;display:flex;justify-content:space-between}
.search-btn{position:absolute;left:52px;top:349px;width:278px;height:52px;background:var(--peach);color:var(--ink);font-size:15px;text-align:center;line-height:52px}
.scroll-cue{position:absolute;left:579px;top:904px;width:42px;height:62px;border-radius:21px;background:var(--white);display:flex;align-items:center;justify-content:center}
.side-dots{position:absolute;left:22px;top:490px;display:flex;flex-direction:column;gap:10px}
.side-dots i{width:6px;height:6px;border-radius:50%;background:var(--white)}

/* services */
.service{position:absolute;top:1032px;width:200px;text-align:center;color:var(--gold)}
.service-art{width:110px;height:110px;margin:0 auto 22px;border-radius:8px;background:linear-gradient(135deg,rgba(231,182,122,.28),rgba(231,182,122,.1))}
.service span{font-family:var(--serif);font-size:18px;letter-spacing:1px}

/* welcome */
.welcome-photo{position:absolute;left:113px;top:1285px;width:478px;height:478px;border-radius:50%;background:radial-gradient(circle at 50% 45%,#e8e6e2 0%,#9aa8bd 30%,#2f5487 70%,#1b3357 100%)}
.badge{position:absolute;left:445px;top:1296px;width:136px;height:136px;border-radius:50%;background:var(--peach);border:4px solid var(--dark);color:var(--ink);text-align:center;font-weight:700}
.badge b{display:block;font-size:56px;line-height:56px;margin-top:20px}
.badge small{font-size:12px}
.dot-ornament{position:absolute;left:158px;top:1684px;width:88px;height:52px;border-radius:6px;background:rgba(231,182,122,.35)}
.eyebrow{font-family:var(--serif);font-size:14px;color:var(--gold);letter-spacing:1px}
.welcome-copy{position:absolute;left:648px;top:1300px;width:460px}
.welcome-copy h2{font-family:var(--serif);font-weight:400;font-size:29px;margin:10px 0 8px}
.welcome-copy .rule{width:90px;height:3px;background:var(--white);margin-bottom:22px}
.welcome-copy p{font-size:12.4px;line-height:17px;margin-bottom:17px}

/* investments */
.invest{left:0;top:1889px;width:1200px;height:816px;background:linear-gradient(180deg,var(--peach-2),var(--peach))}
.section-title{position:absolute;width:1200px;text-align:center;font-family:var(--serif);font-size:29px;letter-spacing:1px;font-weight:400}
.prop-card{position:absolute;top:160px;width:320px;height:484px;background:var(--white);color:var(--ink)}
.prop-photo{height:235px;border-top-right-radius:40px}
.pill{position:absolute;left:42px;top:218px;width:236px;height:40px;border-radius:20px;background:var(--peach);font-family:var(--serif);font-size:12px;text-align:center;line-height:40px;letter-spacing:.5px}
.prop-body{padding:38px 20px 0}
.prop-body h3{font-family:var(--serif);font-weight:400;font-size:18px;line-height:32px;letter-spacing:.5px}
.price{font-family:var(--serif);font-size:12px;color:var(--gold);margin:6px 0 10px}
.ticks{list-style:none;font-size:12.5px;line-height:19px}
.ticks li{display:flex;align-items:center;gap:8px}
.ticks li::before{content:"";width:11px;height:11px;background:var(--ink);border-radius:2px}
.prop-arrow{margin-top:22px}

/* testimonials */
.testimonials{left:0;top:2705px;width:1200px;height:714px;background:linear-gradient(180deg,var(--dark-2) 0%,#242424 60%,#1e1e1e 100%)}
.sub{position:absolute;width:1200px;text-align:center;font-size:12.5px}
.ghost-card{position:absolute;left:239px;top:238px;width:737px;height:284px;border-radius:0 40px 0 0;background:rgba(255,255,255,.06)}
.quote-card{position:absolute;left:291px;top:218px;width:637px;height:326px;border-radius:0 60px 0 40px;background:linear-gradient(135deg,var(--peach),#dfb582);color:var(--ink)}
.avatar{position:absolute;left:41px;top:66px;width:186px;height:186px;border-radius:50%;background:radial-gradient(circle,#e8d3b8 0%,#9e8b7a 60%,#5d6b78 100%)}
.quote-body{position:absolute;left:253px;top:78px;width:345px}
.quote-body h4{font-family:var(--serif);font-weight:400;font-size:15px;letter-spacing:1px}
.quote-body .role{font-size:12.5px;margin:4px 0 20px}
.quote-body p{font-size:12.5px;line-height:19px}
.read-more{display:flex;align-items:center;gap:6px;font-size:12.5px;margin-top:20px}
.stars{position:absolute;left:253px;top:278px;display:flex;gap:5px}
.arrow-btn{position:absolute;top:358px;width:30px;height:30px;border-radius:50%;background:var(--peach);display:flex;align-items:center;justify-content:center}
.carousel-dots{position:absolute;left:580px;top:596px;display:flex;gap:7px}
.carousel-dots i{width:6px;height:6px;border-radius:50%;background:var(--white)}

/* blog */
.blog-band{left:0;top:3419px;width:1200px;height:407px;background:linear-gradient(180deg,var(--peach-2),var(--peach))}
.post{position:absolute;top:3587px;width:320px;height:465px;background:var(--white);color:var(--ink)}
.post-photo{height:239px;border-top-right-radius:40px}
.date{position:absolute;left:20px;top:218px;width:44px;height:46px;background:var(--dark);color:var(--white);font-size:10px;text-align:center;padding-top:6px;line-height:15px}
.post-body{padding:58px 20px 0}
.post-body h3{font-family:var(--serif);font-weight:400;font-size:18px;margin-bottom:26px}
.post-body p{font-size:12.5px;line-height:19px;margin-bottom:24px}

/* contact */
.input{position:absolute;border:1px solid #8a8a8a;font-size:12.5px;padding:14px 12px;color:var(--white)}

/* footer */
.footer-band{left:0;top:4754px;width:1200px;height:500px}
.contact-item{position:absolute;top:4984px;width:240px;text-align:center;font-size:13px;line-height:21px;color:var(--ink)}
.contact-item .ico{width:38px;height:38px;border-radius:50%;background:var(--dark);margin:0 auto 20px;display:flex;align-items:center;justify-content:center}
.newsletter-input{position:absolute;left:446px;top:5148px;width:306px;height:42px;border-radius:21px;background:var(--white);color:#aaa;font-size:13px;font-style:italic;padding:13px 16px}
.newsletter-send{position:absolute;left:760px;top:5148px;width:140px;height:42px;border-radius:21px;background:var(--dark);color:var(--white);font-size:15px;text-align:center;line-height:42px}
.bottom-bar{left:0;top:5254px;width:1200px;height:98px;background:var(--dark)}
.social{position:absolute;top:27px;width:34px;height:34px;border-radius:50%;background:var(--peach)}
</style>
</head>
<body>

<header class="abs site-header">
  <div class="brand" style="left:66px;top:26px;width:200px">
    <span class="brand-square"></span>
    <span class="brand-name">Brisk Vale</span>
  </div>
  <nav class="nav">
    <a class="active" href="#" style="left:461px">Home</a>
    <a href="#" style="left:546px">About us</a>
    <a href="#" style="left:652px">Invesment</a>
    <a href="#" style="left:768px">Finance</a>
    <a href="#" style="left:864px">Blog</a>
  </nav>
  <a class="btn btn-peach" href="#" style="left:938px;top:52px;width:162px;height:50px;text-decoration:none">Contact us
    <span class="dot"><svg width="14" height="14" viewBox="0 0 14 14"><path d="M2 7h9M7 3l4 4-4 4" stroke="#f2c994" stroke-width="2" fill="none"/></svg></span></a>
</header>

<section class="abs hero">
  <div class="hero-photo" role="img" aria-label="Looking up at glass office towers against a cloudy sky"></div>
  <div class="side-dots"><i></i><i></i><i></i></div>
  <h1 class="hero-title">PROPERTY<br>INVESMENT COMPANY</h1>
  <form class="search-panel">
    <div class="search-head">FIND YOUR IDEAL<small>⟵ INVESMENT PROPERTY ⟶</small></div>
    <span class="field-label" style="top:128px">Type of Investment</span>
    <div class="select" style="top:162px"><span>Commerical</span><span>◂</span></div>
    <span class="field-label" style="top:226px">State</span>
    <div class="select" style="top:257px"><span>Washington, DC</span><span>◂</span></div>
    <div class="search-btn">SEARCH INVESTMENT</div>
  </form>
  <svg class="abs" style="left:0;top:620px" width="1200" height="180" viewBox="0 0 1200 180">
    <path d="M0 58 Q600 260 1200 58 L1200 180 L0 180Z" fill="#262626"/>
    <path d="M0 58 Q600 260 1200 58" stroke="#f2c994" stroke-width="8" fill="none"/>
  </svg>
</section>
<div class="scroll-cue"><svg width="14" height="34" viewBox="0 0 14 34"><path d="M7 2v28M2 25l5 6 5-6" stroke="#262626" stroke-width="2" fill="none"/></svg></div>

<section class="services">
  <div class="service" style="left:164px"><div class="service-art" role="img" aria-label="Line illustration of a hand holding a house with money symbols"></div><span>FINANCE</span></div>
  <div class="service" style="left:384px"><div class="service-art" role="img" aria-label="Line illustration of a person beside a rising bar chart"></div><span>INVESTMENT</span></div>
  <div class="service" style="left:618px"><div class="service-art" role="img" aria-label="Line illustration of a hand with a fast moving invoice"></div><span>FAST PROCESS</span></div>
  <div class="service" style="left:853px"><div class="service-art" role="img" aria-label="Line illustration of a consultant at a desk with speech bubble"></div><span>CONSULTING</span></div>
</section>

<section class="welcome">
  <div class="welcome-photo" role="img" aria-label="Cupped hands holding a small model house on a pile of coins"></div>
  <div class="badge"><b>10</b><small>YEAR<br>EXPERIENCE</small></div>
  <div class="dot-ornament" role="img" aria-label="Decorative gold dot pattern"></div>
  <div class="welcome-copy">
    <div class="eyebrow">INVEST FOR YOUR FUTURE</div>
    <h2>WELCOME TO BRISK-VALE</h2>
    <div class="rule"></div>
    <p>Lorem Ipsum is simply dummy text of the printing and typesetting industry has been the industry's standard dummy text ever since the 1500s,</p>
    <p>when an unknown printer took a galley of type and scrambled it to make a type specimen book. It has survived not only five centuries, but also the leap into electronic typesetting, remaining essentially unchanged. It was popularised in the 1960s</p>
    <p>with the release of Typesheet sheets containing Lorem Ipsum passages, and more recently with desktop publishing software like Quillset Layout includingito electronic typesetting, remaining essentially unchanged. It was popularised versions of Lorem Ipsum.</p>
    <p>Lorem Ipsum is simply dummy text of the printing and typesetting industry has been the industry's standard dummy text ever since the 1500s,</p>
  </div>
  <a class="btn btn-peach" href="#" style="left:648px;top:1682px;width:162px;height:46px;text-decoration:none">Read More
    <span class="dot"><svg width="14" height="14" viewBox="0 0 14 14"><path d="M2 7h9M7 3l4 4-4 4" stroke="#f2c994" stroke-width="2" fill="none"/></svg></span></a>
</section>

<section class="abs invest">
  <h2 class="section-title" style="top:82px;color:var(--ink)">INVESTMENT OPPERTUNITY</h2>
  <article class="prop-card" style="left:98px">
    <div class="prop-photo" role="img" aria-label="Modern glass office building" style="background:linear-gradient(160deg,#9fc0de,#3d5a78)"></div>
    <span class="pill">LOS ANGELES, CALIFORNIA</span>
    <div class="prop-body"><h3>EXCLUSIVE PRIVATE GATED RESIDENCY</h3><div class="price">From $00.00</div>
      <ul class="ticks"><li>Huge Groth Expected</li><li>7% Net Return Guatanted for 2 year</li><li>Golden Center Location</li></ul>
      <svg class="prop-arrow" width="22" height="16" viewBox="0 0 22 16"><path d="M1 8h14M10 3l5 5-5 5M19 2v12" stroke="#1f1f1f" stroke-width="2" fill="none"/></svg></div>
  </article>
  <article class="prop-card" style="left:440px">
    <div class="prop-photo" role="img" aria-label="Tall glass office cube under blue sky" style="background:linear-gradient(160deg,#7aa9d4,#2f5e6e)"></div>
    <span class="pill">LOS ANGELES, CALIFORNIA</span>
    <div class="prop-body"><h3>EXCLUSIVE PRIVATE GATED RESIDENCY</h3><div class="price">From $00.00</div>
      <ul class="ticks"><li>Huge Groth Expected</li><li>7% Net Return Guatanted for 2 year</li><li>Golden Center Location</li></ul>
      <svg class="prop-arrow" width="22" height="16" viewBox="0 0 22 16"><path d="M1 8h14M10 3l5 5-5 5M19 2v12" stroke="#1f1f1f" stroke-width="2" fill="none"/></svg></div>
  </article>
  <article class="prop-card" style="left:783px">
    <div class="prop-photo" role="img" aria-label="Curved white apartment balconies" style="background:linear-gradient(160deg,#b9cfe0,#8b8b86)"></div>
    <span class="pill">LOS ANGELES, CALIFORNIA</span>
    <div class="prop-body"><h3>EXCLUSIVE PRIVATE GATED RESIDENCY</h3><div class="price">From $00.00</div>
      <ul class="ticks"><li>Huge Groth Expected</li><li>7% Net Return Guatanted for 2 year</li><li>Golden Center Location</li></ul>
      <svg class="prop-arrow" width="22" height="16" viewBox="0 0 22 16"><path d="M1 8h14M10 3l5 5-5 5M19 2v12" stroke="#1f1f1f" stroke-width="2" fill="none"/></svg></div>
  </article>
  <a class="btn btn-dark" href="#" style="left:519px;top:685px;width:162px;height:48px;text-decoration:none">View More
    <span class="dot"><svg width="14" height="14" viewBox="0 0 14 14"><path d="M2 7h9M7 3l4 4-4 4" stroke="#262626" stroke-width="2" fill="none"/></svg></span></a>
</section>

<section class="abs testimonials">
  <h2 class="section-title" style="top:92px">TESTIMONIALS</h2>
  <p class="sub" style="top:136px">What Clients saying about us</p>
  <div class="ghost-card"></div>
  <div class="quote-card">
    <div class="avatar" role="img" aria-label="Portrait of the client"></div>
    <div class="quote-body">
      <h4>MIRA LANE</h4>
      <div class="role">Creative Director</div>
      <p>Lorem Ipsum is simply dummy text of the printing and typesetting industry has been the industry's standard dummy text ever since the 1500s</p>
      <div class="read-more">Read More.. <svg width="14" height="14" viewBox="0 0 14 14"><circle cx="7" cy="7" r="6" stroke="#1f1f1f" fill="none"/><path d="M4 7h5M7 5l2 2-2 2" stroke="#1f1f1f" fill="none"/></svg></div>
    </div>
    <div class="stars">
      <svg width="104" height="18" viewBox="0 0 104 18" fill="#1f1f1f"><g id="st"><path d="M9 1l2.4 5.3 5.6.5-4.3 3.8 1.3 5.6L9 13.3 4 16.2l1.3-5.6L1 6.8l5.6-.5Z"/></g><use href="#st" x="21"/><use href="#st" x="42"/><use href="#st" x="63"/><use href="#st" x="84"/></svg>
    </div>
  </div>
  <div class="arrow-btn" style="left:224px"><svg width="14" height="14" viewBox="0 0 14 14"><path d="M12 7H3M7 3L3 7l4 4" stroke="#262626" stroke-width="2" fill="none"/></svg></div>
  <div class="arrow-btn" style="left:959px"><svg width="14" height="14" viewBox="0 0 14 14"><path d="M2 7h9M7 3l4 4-4 4" stroke="#262626" stroke-width="2" fill="none"/></svg></div>
  <div class="carousel-dots"><i></i><i></i><i></i></div>
</section>

<section class="blog">
  <div class="abs blog-band"></div>
  <h2 class="section-title" style="top:3512px;color:var(--ink)">OUR BLOG</h2>
  <article class="post" style="left:98px">
    <div class="post-photo" role="img" aria-label="Two glass towers seen from below" style="background:linear-gradient(160deg,#c5d4e4,#4a5f78)"></div>
    <div class="date">21<br>Aug</div>
    <div class="post-body" style="padding-top:64px"><h3>Blog Title Heading</h3>
      <p>Lorem Ipsum is simply dummy text of the print and typesetting industry has been the industry dummy text ever since the 1500s</p>
      <div class="read-more">Read More.. <svg width="14" height="14" viewBox="0 0 14 14"><circle cx="7" cy="7" r="6" stroke="#1f1f1f" fill="none"/><path d="M4 7h5M7 5l2 2-2 2" stroke="#1f1f1f" fill="none"/></svg></div></div>
  </article>
  <article class="post" style="left:440px">
    <div class="post-photo" role="img" aria-label="City skyline with a construction crane" style="background:linear-gradient(180deg,#cfd3d6,#6d7480)"></div>
    <div class="date">21<br>Aug</div>
    <div class="post-body"><h3>Blog Title Heading</h3>
      <p>Lorem Ipsum is simply dummy text of the print and typesetting industry has been the industry dummy text ever since the 1500s</p>
      <div class="read-more">Read More.. <svg width="14" height="14" viewBox="0 0 14 14"><circle cx="7" cy="7" r="6" stroke="#1f1f1f" fill="none"/><path d="M4 7h5M7 5l2 2-2 2" stroke="#1f1f1f" fill="none"/></svg></div></div>
  </article>
  <article class="post" style="left:783px">
    <div class="post-photo" role="img" aria-label="Tower under construction with crane on grey sky" style="background:linear-gradient(180deg,#b5b9bd,#4d5258)"></div>
    <div class="date">21<br>Aug</div>
    <div class="post-body"><h3>Blog Title Heading</h3>
      <p>Lorem Ipsum is simply dummy text of the print and typesetting industry has been the industry dummy text ever since the 1500s</p>
      <div class="read-more">Read More.. <svg width="14" height="14" viewBox="0 0 14 14"><circle cx="7" cy="7" r="6" stroke="#1f1f1f" fill="none"/><path d="M4 7h5M7 5l2 2-2 2" stroke="#1f1f1f" fill="none"/></svg></div></div>
  </article>
  <a class="btn btn-peach" href="#" style="left:513px;top:4100px;width:164px;height:48px;text-decoration:none">View More
    <span class="dot"><svg width="14" height="14" viewBox="0 0 14 14"><path d="M2 7h9M7 3l4 4-4 4" stroke="#f2c994" stroke-width="2" fill="none"/></svg></span></a>
</section>

<section class="contact">
  <h2 class="section-title" style="top:4222px">CONTACT US</h2>
  <div class="input" style="left:293px;top:4285px;width:297px;height:46px">First Name</div>
  <div class="input" style="left:608px;top:4285px;width:299px;height:46px">Last Name</div>
  <div class="input" style="left:293px;top:4354px;width:297px;height:47px">Email</div>
  <div class="input" style="left:608px;top:4354px;width:299px;height:47px">Phone</div>
  <div class="input" style="left:293px;top:4422px;width:614px;height:160px">Message</div>
  <a class="btn btn-peach" href="#" style="left:513px;top:4613px;width:164px;height:52px;text-decoration:none;padding-left:58px">Send
    <span class="dot"><svg width="14" height="14" viewBox="0 0 14 14"><path d="M1 7l12-6-4 12-2-5z" fill="#f2c994"/></svg></span></a>
</section>

<footer>
  <svg class="abs footer-band" width="1200" height="500" viewBox="0 0 1200 500" role="img" aria-label="Faint city skyline silhouette on warm band">
    <defs><linearGradient id="fb" x1="0" y1="0" x2="0" y2="1"><stop offset="0" stop-color="#f2c994"/><stop offset="1" stop-color="#e3b781"/></linearGradient></defs>
    <path d="M0 114 Q600 -60 1200 114 V500 H0Z" fill="url(#fb)"/>
  </svg>
  <div class="brand" style="left:500px;top:4806px;width:200px">
    <span class="brand-square" style="border-color:var(--ink)"></span>
    <span class="brand-name" style="color:var(--ink)">Brisk Vale</span>
  </div>
  <div class="abs serif" style="left:0;top:4944px;width:1200px;text-align:center;font-size:14px;color:var(--ink);letter-spacing:1px">CONTACT US</div>
  <div class="contact-item" style="left:223px"><div class="ico"><svg width="16" height="16" viewBox="0 0 16 16"><path d="M3 1l3 3-2 2q2 4 6 6l2-2 3 3-2 2Q5 15 1 3Z" fill="#f2c994"/></svg></div>555 014 2863</div>
  <div class="contact-item" style="left:476px"><div class="ico"><svg width="16" height="18" viewBox="0 0 16 18"><path d="M8 17S2 10 2 6.5a6 6 0 0112 0C14 10 8 17 8 17Z" fill="#f2c994"/><circle cx="8" cy="6.5" r="2.2" fill="#262626"/></svg></div>1234 Alder Crest Ave<br>#8002, Marlow, GA 12345</div>
  <div class="contact-item" style="left:710px"><div class="ico"><svg width="18" height="14" viewBox="0 0 18 14"><rect x="1" y="1" width="16" height="12" fill="#f2c994"/><path d="M1 1l8 7 8-7" stroke="#262626" fill="none"/></svg></div>info@brisk-vale.com</div>
  <div class="abs serif" style="left:272px;top:5156px;font-size:19px;color:var(--ink);letter-spacing:1px">NEWSLETTER</div>
  <div class="newsletter-input">Your Email Address</div>
  <div class="newsletter-send">Send</div>
  <div class="abs bottom-bar">
    <p class="abs" style="left:98px;top:38px;font-size:13px">Copyright © 2021 <span style="color:var(--peach)">BRISK VALE GROUP</span>, All Rights Reserved.</p>
    <span class="social" style="left:911px"></span>
    <span class="social" style="left:962px"></span>
    <span class="social" style="left:1013px"></span>
    <span class="social" style="left:1065px"></span>
  </div>
</footer>

</body>
</html>
```